1-3 PAGE WEBSITE LANDING PAGE DESIGN FOR REELPITCH.NET

I NEED A DESIGNER THAT HAS A GOOD UNDERSTANDING OF BUSINESS AND MARKETING SO HE CAN TAKE MY SALES SCRIPT AND CONVERT IT INTO A BEAUTIFUL IMAGE AND VIDEO FILLED WEBSITE THAT EXPLAINS EACH POINT BEAUTIFULLY. THE WEBSITE SHOULD BE EASY TO READ AND UNDERSTAND AND NAVIGATE.

PLEASE INCLUDE A EXAMPLES SECTION THAT CAN BE FILTERED BY INDUSTRY.

UNDER EVERY SECTION ON THE WEBSITE WE NEED TO HAVE A CALL TO ACTION BUTTON THAT WILL POP UP INTO A LEAD GEN FORM. THE BUTTON WILL SAY "SIGN UP FOR A FREE VIDEO AD MOCK UP FOR YOUR BUSINESS. No Purchase Necessary."

PLEASE SEE ATTACHED FILES FOR WORD DOC OF CONTENT AND LOGO FOR REELPITCH.NET

Target Market(s)

ALL BUSINESSES WHO WILL BE USING VIDEO ADVERTISEMENT AS PART OF THEIR OVERALL MARKETING STRATEGY FOR YEARS TO COME

Industry/Entity Type

Digital Marketing

Number of Pages Required

2 page

Colors

Designer to choose colors to be used in the design.

Requirements
Must have
• I would like color theme to coordinate with logo color theme
Nice to have
• must include all content included in word document

```html
<!DOCTYPE html>
<html lang="en">
<head>
<meta charset="utf-8">
<title>REELPITCH.NET – Video Ads</title>
<link href="https://fonts.googleapis.com/css2?family=Open+Sans:wght@400;600;700;800&display=swap" rel="stylesheet">
<style>
:root{
  --yellow:#fff200;
  --black:#0d0d0d;
  --ink:#111111;
  --white:#ffffff;
  --pale-blue:#dce7f0;
  --footer-grey:#ececec;
  --muted:#a9a9a9;
  --text:#333333;
  --navy:#050a2a;
}
*{box-sizing:border-box;margin:0;padding:0}
html,body{width:1200px;height:5241px;overflow:hidden}
body{font-family:"Open Sans",Arial,sans-serif;color:var(--text);background:var(--white);position:relative}
.btn{display:flex;align-items:center;justify-content:center;text-align:center;background:var(--yellow);color:#111;font-size:12.5px;line-height:1.45;text-transform:uppercase;text-decoration:none;position:absolute}
.photo{position:absolute}

/* header */
.site-header{position:absolute;top:0;left:0;width:1200px;height:98px;background:var(--white);border-bottom:1px solid #e5e5e5}
.brand{position:absolute;left:112px;top:30px;display:flex;align-items:center;gap:10px;font-weight:800;font-size:30px;color:#222;letter-spacing:1px}
.brand-dot{width:22px;height:22px;border-radius:50%;background:var(--yellow)}
.main-nav{position:absolute;right:112px;top:34px;display:flex;gap:10px}
.main-nav a{font-size:13.5px;color:#222;text-decoration:none;padding:7px 20px}
.main-nav a.active{background:var(--yellow);font-weight:700}

/* hero */
.hero{position:absolute;top:98px;left:0;width:1200px;height:465px;background:#000}
.hero .photo{inset:0;background:radial-gradient(ellipse at 75% 40%,#3a3020 0%,#1a1510 45%,#050505 80%)}
.hero h1{position:absolute;left:112px;top:84px;font-size:45px;line-height:54px;font-weight:700;color:var(--white);text-transform:uppercase}
.hero h1 span{color:var(--yellow)}
.hero p{position:absolute;left:112px;top:204px;width:670px;font-size:13px;line-height:22px;color:#eee}
.hero .btn{left:112px;top:315px;width:366px;height:62px}
.hero-dots{position:absolute;left:1075px;top:208px;display:flex;flex-direction:column;gap:12px}
.hero-dots i{width:12px;height:12px;border-radius:50%;border:2px solid var(--yellow);display:block}

/* intro cards */
.intro-card{position:absolute;top:655px;width:474px;height:417px;background:#1b1b1b;overflow:hidden}
.intro-card .photo{inset:0;background:linear-gradient(135deg,#2b2b2b,#121212 60%,#3a3a3a)}
.intro-card .frame{position:absolute;left:52px;top:56px;width:385px;height:240px;border:1.5px solid var(--yellow);border-left:none;border-bottom:none}
.intro-card h3{position:absolute;left:52px;top:48px;background:transparent;padding-right:14px;font-size:15px;line-height:26px;font-weight:600;color:var(--white);text-transform:uppercase}
.intro-card p{position:absolute;left:52px;width:330px;font-size:12.5px;line-height:22px;color:#ddd}
.intro-card .btn{left:52px;top:300px;width:366px;height:62px}

/* features */
.features{position:absolute;top:1163px;left:0;width:1200px;height:1176px;background:var(--pale-blue)}
.feature{position:absolute;left:112px;width:976px;height:245px;background:var(--black)}
.feature .photo{top:0;width:332px;height:245px;background:linear-gradient(135deg,#5a5248,#2c2824)}
.feature .play{position:absolute;top:102px;width:44px;height:44px;border:2px solid #fff;border-radius:50%}
.feature .play::after{content:"";position:absolute;left:16px;top:12px;border-left:13px solid #fff;border-top:8px solid transparent;border-bottom:8px solid transparent}
.feature h2{position:absolute;top:36px;font-size:22px;font-weight:600;color:var(--yellow);text-transform:uppercase}
.feature .copy{position:absolute;font-size:12.5px;line-height:22px;color:var(--muted)}
.feature .copy strong{color:#eee;font-weight:400;display:block}
.feature .btn{width:366px;height:62px}
.feature.text-left .photo{right:0}
.feature.text-left h2,.feature.text-left .copy,.feature.text-left .btn{left:20px}
.feature.text-left .play{right:144px}
.feature.text-right .photo{left:0}
.feature.text-right h2,.feature.text-right .copy,.feature.text-right .btn{left:370px}
.feature.text-right .play{left:144px}

/* formats */
.formats{position:absolute;top:2396px;left:0;width:1200px;height:692px;background:radial-gradient(ellipse at 80% 50%,#0c1a66 0%,var(--navy) 60%)}
.formats h2{position:absolute;top:44px;width:100%;text-align:center;font-size:21px;line-height:35px;font-weight:700;color:var(--yellow);text-transform:uppercase}
.formats .body{position:absolute;top:150px;left:140px;width:920px;text-align:center;font-size:12.5px;line-height:22px;color:#e8e8f2}
.formats .body p{margin-bottom:22px}
.formats .btn{left:416px;top:552px;width:366px;height:62px}

/* process */
.process{position:absolute;top:3088px;left:0;width:1200px;height:1198px;background:var(--pale-blue)}
.section-title{position:absolute;width:100%;text-align:center;font-size:44px;font-weight:700;color:#111;text-transform:uppercase}
.process .section-title{top:76px}
.step{position:absolute;width:448px;height:443px;background:var(--black)}
.step h3{position:absolute;left:41px;top:60px;width:360px;font-size:21px;line-height:35px;font-weight:400;color:var(--white);text-transform:uppercase}
.step p{position:absolute;left:41px;width:360px;font-size:12.5px;line-height:22px;color:var(--muted)}
.step .btn{left:41px;top:318px;width:366px;height:62px}

/* gallery */
.gallery .section-title{top:4358px}
.thumb{position:absolute;top:4475px;width:310px;height:254px;background:linear-gradient(135deg,#7a6e5c,#3a342c)}
.thumb .play{position:absolute;left:133px;top:105px;width:44px;height:44px;border:2px solid #fff;border-radius:50%}
.thumb .play::after{content:"";position:absolute;left:16px;top:12px;border-left:13px solid #fff;border-top:8px solid transparent;border-bottom:8px solid transparent}

/* footer */
.site-footer{position:absolute;top:4831px;left:0;width:1200px;height:335px;background:var(--footer-grey)}
.site-footer .brand{top:90px}
.contact{position:absolute;left:112px;top:193px;list-style:none}
.contact li{display:flex;align-items:center;gap:18px;font-size:13px;color:#555;height:31px}
.contact svg{width:14px;height:14px}
.footer-col h4{position:absolute;top:92px;font-size:15px;font-weight:600;color:#222}
.quick-links{position:absolute;left:582px;top:128px;list-style:none}
.quick-links li{font-size:13px;color:#555;height:26px;padding-left:22px;position:relative}
.quick-links li::before{content:"›";position:absolute;left:0;color:#999}
.footer-gallery{position:absolute;left:816px;top:130px;display:grid;grid-template-columns:repeat(3,86px);gap:8px 8px}
.footer-gallery div{height:50px;background:linear-gradient(135deg,#5a5c70,#2a2a38)}
.copyright-bar{position:absolute;top:5166px;left:0;width:1200px;height:75px;background:var(--ink)}
.copyright-bar p{position:absolute;left:112px;top:29px;font-size:11px;color:#aaa}
.social{position:absolute;right:112px;top:30px;display:flex;gap:22px}
.social i{width:14px;height:14px;border-radius:50%;background:var(--yellow);display:block}
</style>
</head>
<body>

<header class="site-header">
  <div class="brand"><span class="brand-dot"></span>REELPITCH.NET</div>
  <nav class="main-nav">
    <a class="active" href="#">Home</a><a href="#">About Us</a><a href="#">Services</a><a href="#">Video Gallery</a><a href="#">Contact Us</a>
  </nav>
</header>

<section class="hero">
  <div class="photo" role="img" aria-label="Person silhouetted before a wall of glowing video screens"></div>
  <h1><span>Video Ads</span> for promoting<br>your special offers</h1>
  <p>We are a video production company that specializes in short, entertaining mini commercial type of video "ADS" ("ADVERTISEMENTS") FULLY CUSTOMIZED AND BRANDED TO YOUR BUSINESS, using premium stock footage. Our video ads grab attention within just a few seconds and get the call to action across quickly such as clicking through to your website and opting into a webform or simply contacting your business.</p>
  <a class="btn" href="#">Sign up for a free video ad mock up<br>for your business. No purchase necessary</a>
  <div class="hero-dots"><i></i><i></i><i></i></div>
</section>

<article class="intro-card" style="left:112px">
  <div class="photo" role="img" aria-label="Laptop showing sales charts on a desk"></div>
  <div class="frame"></div>
  <h3 style="background:#1e1e1e">Promote special deals</h3>
  <p style="top:100px">They are used to advertise special offers (discounts, limited time deals, Holiday promotions, free quote, BOGO, free shipping, etc.) on your website and social media.</p>
  <a class="btn" href="#">Sign up for a free video ad mock up<br>for your business. No purchase necessary</a>
</article>

<article class="intro-card" style="left:614px">
  <div class="photo" role="img" aria-label="Workspace with a laptop and notebook"></div>
  <div class="frame"></div>
  <h3 style="background:#1e1e1e">Order, revise, approve, step by<br>step email notices</h3>
  <p style="top:122px">Ordering video ads is super simple too. You simply tell us what you want to promote and we deliver the video mockup in as little as 24 hours. You can login to your account 24/7 to view, approve and revise all the video ads we make for you. We also notify you by email every step of the way, so if it's easier for you, everything can be handled by email.</p>
  <a class="btn" href="#">Sign up for a free video ad mock up<br>for your business. No purchase necessary</a>
</article>

<section class="features">
  <article class="feature text-left" style="top:57px">
    <div class="photo" role="img" aria-label="Woman smiling while working on a laptop"></div><span class="play"></span>
    <h2>Done for you content</h2>
    <p class="copy" style="top:78px;width:560px">You can provide the content or we can come up with content for you. This really is a "done for you" service.</p>
    <a class="btn" href="#" style="top:140px">Sign up for a free video ad mock up<br>for your business. No purchase necessary</a>
  </article>
  <article class="feature text-right" style="top:328px">
    <div class="photo" role="img" aria-label="Two colleagues reviewing a tablet in a warehouse"></div><span class="play"></span>
    <h2>Unlimited revisions</h2>
    <p class="copy" style="top:78px;width:570px">We give you UNLIMITED REVISIONS. Our goal is to provide you with a video ad that you can be proud of.</p>
    <a class="btn" href="#" style="top:140px">Sign up for a free video ad mock up<br>for your business. No purchase necessary</a>
  </article>
  <article class="feature text-left" style="top:596px">
    <div class="photo" role="img" aria-label="Couple looking at a phone together"></div><span class="play"></span>
    <h2>You have full ownership of videos</h2>
    <p class="copy" style="top:78px;width:580px">The videos are fully licensed to you so you own them outright, 100%, forever. All final video files are Full HD (1080p) in Mp4 Format.</p>
    <a class="btn" href="#" style="top:140px">Sign up for a free video ad mock up<br>for your business. No purchase necessary</a>
  </article>
  <article class="feature text-right" style="top:867px">
    <div class="photo" role="img" aria-label="Young couple smiling at a smartphone"></div><span class="play"></span>
    <h2>Pricing</h2>
    <p class="copy" style="top:70px;width:570px"><strong>PACKAGES STARTING AT JUST $37/VIDEO AND ONLY $16/VIDEO</strong>We have pkgs starting at just $37/video. When we create a video ad for you we actually provide you with 4 video formats all FULL HD 1080p, basically 4 separate video files.</p>
    <a class="btn" href="#" style="top:155px">Sign up for a free video ad mock up<br>for your business. No purchase necessary</a>
  </article>
</section>

<section class="formats">
  <h2>4 essential video formats for<br>all your online digital marketing requirements</h2>
  <div class="body">
    <p>You'll get the widescreen format which is compatible with virtually every online platform out there. We're also going to give you a larger square format which is key for Friendbook specifically as it takes up more real estate on your posts and advertisements making them stand out more.</p>
    <p>We also include a Vertical format (tall rectangular shape) which is essential to your social media marketing as it is formatted perfectly for Friendbook, Photogram and Flashchat STORIES.....</p>
    <p>The 4th format is called the Friendbook Cover Video. This is a video format that you can upload to your companies Friendbook Business Page. You know the main banner where most businesses use an image, well Friendbook recently enabled the ability for you to now put a video there. So this is also included in this package and will definitely make your Friendbook business page pop.</p>
    <p>So its 4 essential video formats that will cover all your video marketing requirements, for just $149 which comes out to just $37 a video format.</p>
    <p>OR</p>
    <p>You can sign up for a subscription where you can get a brand new video ad every month to help you keep your ads fresh and exciting month in and month out and you'll get the same 4 video formats $99 a month, comes out to just $25 a video.</p>
  </div>
  <a class="btn" href="#">Sign up for a free video ad mock up<br>for your business. No purchase necessary</a>
</section>

<section class="process">
  <h2 class="section-title">Our video making process</h2>
  <article class="step" style="left:112px;top:191px">
    <h3>Library of millions of premium stock footage and images</h3>
    <p style="top:188px">We have access to over 15 million stock video clips and over 8 million stock images that we use to create these video ads (we can even integrate your high resolution images as well).</p>
    <a class="btn" href="#">Sign up for a free video ad mock up<br>for your business. No purchase necessary</a>
  </article>
  <article class="step" style="left:639px;top:191px">
    <h3>Library of millions of premium stock footage and images</h3>
    <p style="top:188px">We have access to over 15 million stock video clips and over 8 million stock images that we use to create these video ads (we can even integrate your high resolution images as well).</p>
    <a class="btn" href="#">Sign up for a free video ad mock up<br>for your business. No purchase necessary</a>
  </article>
  <article class="step" style="left:112px;top:669px">
    <h3>Fully customized video ads with full branding</h3>
    <p style="top:150px">We then fully customize the raw footage by adding content/text on top of each transition/segment within the video ad. The transition/segment is basically every time the text or an image or both change within the video.</p>
    <a class="btn" href="#">Sign up for a free video ad mock up<br>for your business. No purchase necessary</a>
  </article>
  <article class="step" style="left:639px;top:669px">
    <h3>Use your content, your video footage, your music</h3>
    <p style="top:150px">So if you have specific ideas, desires, requirements, please tell us what they are.. like specific types of footage or images you would like to see integrated into the video, this is the kind of details and feedback we love because we have a very high success rate at finding exact footage that you ask for or something super close.</p>
    <a class="btn" href="#" style="top:344px">Sign up for a free video ad mock up<br>for your business. No purchase necessary</a>
  </article>
</section>

<section class="gallery">
  <h2 class="section-title">Video gallery</h2>
  <div class="thumb" style="left:112px" role="img" aria-label="Hands arranging printed photos on a desk"><span class="play"></span></div>
  <div class="thumb" style="left:445px;background:linear-gradient(135deg,#55585e,#222428)" role="img" aria-label="Film crew operating a camera on set"><span class="play"></span></div>
  <div class="thumb" style="left:779px;background:linear-gradient(135deg,#d8d8d8,#8a8a8a)" role="img" aria-label="Man with headphones editing video"><span class="play"></span></div>
</section>

<footer class="site-footer">
  <div class="brand"><span class="brand-dot"></span>REELPITCH.NET</div>
  <ul class="contact">
    <li><svg viewBox="0 0 14 14"><path d="M7 0a5 5 0 0 0-5 5c0 4 5 9 5 9s5-5 5-9a5 5 0 0 0-5-5zm0 7a2 2 0 1 1 0-4 2 2 0 0 1 0 4z" fill="#111"/></svg>Lorem Ipsum Dolor Sit</li>
    <li><svg viewBox="0 0 14 14"><path d="M3 1l2 3-1.3 1.3a8 8 0 0 0 5 5L10 9l3 2-1 2.5C6 13 1 8 .5 2z" fill="#111"/></svg>(000) 0000 0000 00</li>
    <li><svg viewBox="0 0 14 14"><rect x="0.5" y="2.5" width="13" height="9" fill="#111"/><path d="M1 3l6 4.5L13 3" stroke="#fff" fill="none"/></svg>yourmail@reelpitch.net</li>
  </ul>
  <div class="footer-col"><h4 style="left:582px">Quick Links</h4></div>
  <ul class="quick-links">
    <li>Home</li><li>About Us</li><li>Services</li><li>Video</li><li>Gallery</li><li>Contact Us</li>
  </ul>
  <div class="footer-col"><h4 style="left:816px">Gallery</h4></div>
  <div class="footer-gallery" role="img" aria-label="Six small video stills">
    <div></div><div style="background:linear-gradient(135deg,#7a4ac0,#2a1a60)"></div><div></div>
    <div style="background:linear-gradient(135deg,#4a3a30,#1a1410)"></div><div style="background:linear-gradient(135deg,#c06040,#402018)"></div><div style="background:linear-gradient(135deg,#aab,#667)"></div>
  </div>
</footer>

<div class="copyright-bar">
  <p>Copyright @ 2019 REELPITCH.NET. All Rights Reserved</p>
  <div class="social"><i></i><i></i><i></i></div>
</div>

</body>
</html>
```